Orva Business Card

we need a business card for flooring business called Orva Flooring, the design should be black and white. we have 2 locations

Halverton Showroom
527 Kellerman Road,
Halverton VIC 3158

Ashcombe Showroom
462 Bramwell Hwy,
Ashcombe VIC 3219

email : sales@orvaflooring.com.au
(03) 9471 2830

Please inform we sell , Laminate, Hybrid, Timber, carpet and commercial flooring

```html
<!DOCTYPE html>
<html lang="en">
<head>
<meta charset="utf-8">
<title>Orva Flooring — Business Card</title>
<link href="https://fonts.googleapis.com/css2?family=Figtree:wght@400;500&display=swap" rel="stylesheet">
<style>
  :root {
    --ink: #000000;
    --paper: #ffffff;
    --page: #ffffff;
  }
  * { box-sizing: border-box; margin: 0; padding: 0; }
  html, body {
    width: 1037px; height: 1200px; overflow: hidden;
    background: var(--page);
    font-family: "Figtree", Arial, sans-serif;
  }
  .canvas { position: relative; width: 1037px; height: 1200px; }
  .card {
    position: absolute; left: 33px; width: 970px; height: 558px;
    --fg: var(--ink); --bg: var(--paper);
    background: var(--bg); color: var(--fg);
  }
  .card--light { top: 36px; border: 2px solid var(--ink); }
  .card--dark { top: 617px; --fg: var(--paper); --bg: var(--ink); }
  .card__content { position: absolute; left: 168px; top: 0; width: 680px; height: 100%; }
  .card--dark .card__content { left: 156px; top: -1px; }
  .card--dark .wordmark { left: 592px; top: 132px; }
  .card__title { position: absolute; top: 101px; left: 0; font-size: 25px; font-weight: 500; }
  .card--dark .card__title { font-weight: 400; }
  .info { position: absolute; left: 1px; font-size: 17.5px; line-height: 19.5px; font-weight: 400; white-space: nowrap; }
  .info--north { top: 147px; }
  .info--south { top: 239px; }
  .info--contact { top: 331px; font-size: 18.5px; line-height: 20.5px; }
  .rule { position: absolute; left: 1px; height: 1px; background: var(--fg); }
  .rule--short { width: 367px; }
  .rule--one { top: 218px; }
  .rule--two { top: 313px; }
  .rule--long { top: 385px; width: 637px; }
  .card--dark .rule--long { width: 661px; }
  .range { position: absolute; top: 393px; left: -6px; font-size: 23.5px; line-height: 26px; font-weight: 500; white-space: nowrap; }
  .card--dark .range { font-weight: 400; }
  .wordmark {
    position: absolute; left: 583px; top: 135px; width: 212px; height: 184px;
    display: flex; flex-direction: column; align-items: center; justify-content: center;
    color: var(--fg); font-weight: 400; text-align: center;
  }
  .wordmark__name { font-size: 64px; line-height: 1; letter-spacing: 1px; }
  .wordmark__trade { font-size: 34px; line-height: 1.2; letter-spacing: 1px; text-transform: uppercase; }
</style>
</head>
<body>
<main class="canvas">
  <section class="card card--light" aria-label="Business card, light side">
    <div class="card__content">
      <h1 class="card__title">Orva Flooring</h1>
      <p class="info info--north">Halverton Showroom<br>527 Kellerman Road,<br>Halverton VIC 3158</p>
      <div class="rule rule--short rule--one"></div>
      <p class="info info--south">Ashcombe Showroom<br>462 Bramwell Hwy,<br>Ashcombe VIC 3219</p>
      <div class="rule rule--short rule--two"></div>
      <p class="info info--contact">Email: sales@orvaflooring.com.au<br>Phone: (03) 9471 2830</p>
      <div class="rule rule--long"></div>
      <p class="range">We sell:<br>Laminate, Hybrid, Timber, Carpet, and Commercial Flooring</p>
    </div>
    <div class="wordmark"><span class="wordmark__name">Orva</span><span class="wordmark__trade">Flooring</span></div>
  </section>

  <section class="card card--dark" aria-label="Business card, dark side">
    <div class="card__content">
      <h2 class="card__title">Orva Flooring</h2>
      <p class="info info--north">Halverton Showroom<br>527 Kellerman Road,<br>Halverton VIC 3158</p>
      <div class="rule rule--short rule--one"></div>
      <p class="info info--south">Ashcombe Showroom<br>462 Bramwell Hwy,<br>Ashcombe VIC 3219</p>
      <div class="rule rule--short rule--two"></div>
      <p class="info info--contact">Email: sales@orvaflooring.com.au<br>Phone: (03) 9471 2830</p>
      <div class="rule rule--long"></div>
      <p class="range">We sell:<br>Laminate, Hybrid, Timber, Carpet, and Commercial Flooring</p>
    </div>
    <div class="wordmark"><span class="wordmark__name">Orva</span><span class="wordmark__trade">Flooring</span></div>
  </section>
</main>
</body>
</html>
```